Modern business card design for professional copywriter

I'd like a business card design that I can use to have my cards printed out by plink.com as a squared corners business card (see artwork and design guidelines here: https://help.plink.com/hc/en-gb/sections/300481726-PLINK-Product-Templates)

The design should be clean and modern and reflect the colours, tone and branding on my website: https://noravestrel.com.au

Target Market(s)

Professionals, B2B small business owners

Industry/Entity Type

Business

Contact Information for Business Card

Nora Vestrel
m: 0427 593 864
e: nora@noravestrel.com.au
w: noravestrel.com.au

Font styles to use
Sans Serif

Requirements
Must have
• Tagline: "Sharp words that help busy businesses grow"
• Brand colours: fd8000, 009984, 666666 and black
Nice to have

```html
<!DOCTYPE html>
<html lang="en">
<head>
<meta charset="utf-8">
<title>Nora Vestrel — Business Card</title>
<link rel="stylesheet" href="https://fonts.googleapis.com/css2?family=Montserrat:wght@400;500;700&display=swap">
<style>
  :root {
    --orange: #fd8000;
    --teal: #009984;
    --grey: #666666;
    --black: #000000;
    --card: #ffffff;
    --backdrop: #a7a8ab;
  }
  * { margin: 0; padding: 0; box-sizing: border-box; }
  html, body {
    width: 1200px; height: 934px; overflow: hidden;
    background: var(--backdrop);
    font-family: "Montserrat", sans-serif;
  }
  .card {
    position: absolute; left: 264px; width: 683px; height: 390px;
    background: var(--card); border-radius: 16px;
  }
  .card--front { top: 56px; }
  .card--back { top: 481px; }

  .brand { display: flex; align-items: center; gap: 8px; position: absolute; }
  .brand__dot { width: 16px; height: 16px; border-radius: 50%; background: var(--orange); }
  .brand__name { font-weight: 500; font-size: 30px; color: var(--teal); letter-spacing: -0.5px; }
  .card--front .brand { right: 41px; top: 98px; }
  .card--back .brand { left: 0; right: 0; justify-content: center; top: 166px; }

  .holder {
    position: absolute; left: 53px; top: 226px;
    font-weight: 700; font-size: 29px; color: var(--grey);
  }
  .rule {
    position: absolute; left: 53px; top: 281px; width: 580px; height: 2px; background: var(--black);
  }
  .contacts { position: absolute; left: 53px; top: 295px; list-style: none; }
  .contacts li {
    display: flex; align-items: center; gap: 17px;
    height: 23px; font-size: 19px; color: var(--grey);
  }
  .contacts svg { width: 17px; height: 17px; flex: none; }
  .contacts .strong { color: var(--black); }

  .tagline {
    position: absolute; left: 0; right: 0; top: 233px; text-align: center;
    font-size: 19px; color: var(--grey);
  }
</style>
</head>
<body>
  <section class="card card--front">
    <div class="brand"><span class="brand__dot"></span><span class="brand__name">Nora Vestrel</span></div>
    <h1 class="holder">Nora Vestrel</h1>
    <div class="rule"></div>
    <ul class="contacts">
      <li>
        <svg viewBox="0 0 20 20" aria-hidden="true"><circle cx="10" cy="10" r="10" fill="#666666"/><rect x="6.5" y="4" width="7" height="12" rx="1.2" fill="#fff"/><rect x="7.7" y="5.5" width="4.6" height="7.5" fill="#666666"/></svg>
        <span>0427 593 864</span>
      </li>
      <li>
        <svg viewBox="0 0 20 20" aria-hidden="true"><circle cx="10" cy="10" r="10" fill="#666666"/><rect x="4.5" y="6" width="11" height="8" rx="1" fill="#fff"/><path d="M4.8 6.5 10 10.5l5.2-4" fill="none" stroke="#666666" stroke-width="1.2"/></svg>
        <span>nora@<span class="strong">noravestrel</span>.com.au</span>
      </li>
      <li>
        <svg viewBox="0 0 20 20" aria-hidden="true"><circle cx="10" cy="10" r="10" fill="#666666"/><g fill="none" stroke="#fff" stroke-width="1"><circle cx="10" cy="10" r="6"/><ellipse cx="10" cy="10" rx="2.6" ry="6"/><path d="M4 10h12M5 7h10M5 13h10"/></g></svg>
        <span>noravestrel.com.au</span>
      </li>
    </ul>
  </section>

  <section class="card card--back">
    <div class="brand"><span class="brand__dot"></span><span class="brand__name">Nora Vestrel</span></div>
    <p class="tagline">"Sharp words that help busy businesses grow"</p>
  </section>
</body>
</html>
```